Geschäftspapiere für Unternehmensberatung
Zielgruppe
Unternehmensberatung,
Vorstände, Geschäftsführer, Personalleiter, Führungskräfte
Aufgabenstellung
Das Briefpapier muss veränderbar sein, da die Daten sich noch ändern werden. Diese liegen aber erst nach der Ummeldung im Handelsregister endgültig vor.
Eine Vorlage unseres alten Briefpapiers folgt.

```html
<!DOCTYPE html>
<html lang="de">
<head>
<meta charset="utf-8">
<title>Nordhafen Beratungskontor – Briefbogen</title>
<link href="https://fonts.googleapis.com/css2?family=Open+Sans:wght@400;600;700&display=swap" rel="stylesheet">
<style>
  :root {
    --backdrop: #dcdadd;
    --paper: #ffffff;
    --brand-blue: #3f56a3;
    --ink: #161616;
    --rule: #8a8a8a;
  }
  html, body {
    margin: 0;
    width: 1200px;
    height: 1200px;
    overflow: hidden;
    background: var(--backdrop);
    font-family: "Open Sans", sans-serif;
  }
  .letterhead {
    position: absolute;
    left: 302px;
    top: 179px;
    width: 595px;
    height: 842px;
    background: var(--paper);
    color: var(--ink);
  }
  .brand {
    position: absolute;
    left: 68px;
    top: 36px;
    display: flex;
    align-items: center;
    gap: 12px;
  }
  .brand-mark {
    width: 38px;
    height: 38px;
    background: var(--brand-blue);
  }
  .brand-name {
    font-size: 16px;
    font-weight: 600;
    line-height: 1.15;
    letter-spacing: 0.02em;
    color: var(--ink);
  }
  .header-rule {
    position: absolute;
    left: 68px;
    top: 108px;
    width: 500px;
    border-top: 0.8px solid var(--rule);
  }
  .sender-line {
    position: absolute;
    left: 68px;
    top: 141px;
    font-size: 5.6px;
    white-space: nowrap;
  }
  .sender-line .accent { color: var(--brand-blue); font-weight: 700; }
  .sender-line strong { font-weight: 700; }
  .reference-block {
    position: absolute;
    left: 354px;
    top: 140px;
    margin: 0;
    padding: 0;
    list-style: none;
    font-size: 8px;
    font-weight: 600;
    line-height: 12px;
    color: var(--brand-blue);
  }
  .reference-block .gap { height: 12px; }
  .fold-mark {
    position: absolute;
    left: 0;
    width: 20px;
    border-top: 0.8px solid var(--ink);
  }
  .fold-mark.first { top: 297px; border-color: var(--brand-blue); }
  .fold-mark.second { top: 420px; }
  .footer-rule {
    position: absolute;
    left: 68px;
    width: 500px;
    border-top: 0.8px solid var(--rule);
  }
  .footer-rule.top { top: 678px; }
  .footer-rule.bottom { top: 784px; }
  .footer-col {
    position: absolute;
    top: 690px;
    font-size: 6.6px;
    line-height: 9px;
    color: var(--ink);
  }
  .footer-col h4 {
    margin: 0 0 9px;
    font-size: 6.8px;
    font-weight: 700;
    color: var(--brand-blue);
  }
  .footer-col p { margin: 0 0 9px; }
  .footer-col.company { left: 68px; }
  .footer-col.management { left: 245px; }
  .footer-col.register { left: 355px; }
  .footer-col.bank { left: 463px; }
  .tagline-band {
    position: absolute;
    left: 68px;
    top: 802px;
    width: 500px;
    height: 40px;
    background: var(--brand-blue);
    color: #fff;
    font-size: 13.6px;
    font-weight: 600;
    letter-spacing: 0.02em;
    display: flex;
    align-items: center;
    justify-content: center;
  }
</style>
</head>
<body>
  <main class="letterhead">
    <div class="brand">
      <div class="brand-mark"></div>
      <div class="brand-name">NORDHAFEN<br>BERATUNGSKONTOR</div>
    </div>
    <div class="header-rule"></div>

    <div class="sender-line"><span class="accent">NORDHAFEN</span> <strong>BERATUNGSKONTOR</strong> | Am Lindenhang 7 | 24817 Wiesental</div>

    <ul class="reference-block">
      <li>Ihr Zeichen:</li>
      <li>Ihre Nachricht vom:</li>
      <li>Unser Zeichen:</li>
      <li>Unsere Nachricht vom:</li>
      <li>Beschreibung des Falles:</li>
      <li class="gap"></li>
      <li>Name:</li>
      <li>Telefon:</li>
      <li>Telefax:</li>
      <li>E-Mail:</li>
      <li class="gap"></li>
      <li>Datum:</li>
    </ul>

    <div class="fold-mark first"></div>
    <div class="fold-mark second"></div>

    <div class="footer-rule top"></div>
    <footer>
      <div class="footer-col company">
        <h4>NBK - Nordhafen Beratungskontor GmbH</h4>
        <p>Am Lindenhang 7<br>24817 Wiesental</p>
        <p>Telefon:&nbsp;&nbsp; +49 040 5582310<br>Telefax:&nbsp;&nbsp; +49 040 5582319<br>E-Mail:&nbsp;&nbsp;&nbsp;&nbsp; office@nordhafen-kontor.de<br>Internet: www.nordhafen-kontor.de</p>
      </div>
      <div class="footer-col management">
        <h4>Geschäftsführer</h4>
        <p>Helene Varnholt<br>Jonas Brettlingk</p>
        <h4>Gesellschafter</h4>
        <p>Helene Varnholt<br>Jonas Brettlingk</p>
      </div>
      <div class="footer-col register">
        <h4>Handelsregister</h4>
        <p>Amtsgericht Wiesental<br>HRB 4926 WT</p>
      </div>
      <div class="footer-col bank">
        <h4>Bankverbindung:</h4>
        <p>Musterbank Musterstadt<br>IBAN: DE00123400009876543210<br>BIC:&nbsp;&nbsp;&nbsp; MUSTDE21XXX</p>
      </div>
    </footer>
    <div class="footer-rule bottom"></div>

    <div class="tagline-band">Nordhafen Beratungskontor – Veränderung gemeinsam gestalten</div>
  </main>
</body>
</html>
```